Lumo Nutrition Boost

We need a label designed for 4 different Vitamins. Dr. Lumo is a Chiropractor and would like to add few vitamins that help his patients and other people in need. Our logo is black and white which I will share below. We want something that stands out, attracts all age clients, and is easy to read and remember. Needs to be catchy just like the Brand Name - "Lumo" The Logo will be switched. Instead of it saying Chiropractic & Physical Therapy, it should say Nutrition on top and Boost on the bottom. Below is also my idea roughly on the designs, but open to your ideas and the name is what we want to go with. Also providing couple designs that were worked on under a different account by one of our collaborators. Thank You, Tova

```html
<!DOCTYPE html>
<html lang="en">
<head>
<meta charset="utf-8">
<title>Lumo – Revive Spark Omega-3 Label</title>
<link rel="stylesheet" href="https://fonts.googleapis.com/css2?family=Archivo:wght@400;700&family=Montserrat:wght@400;800;900&display=swap">
<style>
  :root {
    --white: #ffffff;
    --ink: #1e1e1e;
    --deep-purple: #2e1f5e;
    --plum: #5e1a70;
    --grape: #6a1670;
    --magenta: #c5359a;
    --band-purple: #4b2466;
    --cyan: #19c3f0;
    --yellow: #f5c400;
    --rose: #e8175d;
    --trim: #f0d6ef;
  }
  html, body {
    margin: 0;
    padding: 0;
    width: 1200px;
    height: 1200px;
    overflow: hidden;
    background: var(--white);
  }
  .label {
    position: absolute;
    left: 100px;
    top: 491px;
    width: 998px;
    height: 357px;
  }
  .facts-title { font: 700 30px "Archivo", sans-serif; letter-spacing: 1.5px; fill: var(--ink); }
  .facts-small { font: 400 12.5px "Archivo", sans-serif; fill: var(--ink); }
  .facts-bold { font: 700 13px "Archivo", sans-serif; letter-spacing: 1px; fill: var(--ink); }
  .facts-tiny { font: 700 7px "Archivo", sans-serif; letter-spacing: 0.5px; fill: var(--ink); }
  .product-name { font: 900 86px "Montserrat", sans-serif; }
  .product-sub { font: 900 64px "Montserrat", sans-serif; }
  .variant { font: 800 22px "Montserrat", sans-serif; fill: var(--white); }
  .net-weight { font: 800 38px "Montserrat", sans-serif; fill: var(--band-purple); }
  .brand-name { font: 800 34px "Montserrat", sans-serif; fill: var(--white); }
  .body-copy { font: 400 12.8px "Montserrat", sans-serif; fill: var(--ink); }
</style>
</head>
<body>
<svg class="label" viewBox="125 614 1248 446" xmlns="http://www.w3.org/2000/svg" aria-label="Revive Spark Omega-3 bottle label">
  <defs>
    <linearGradient id="wave-gradient" x1="0" y1="0" x2="1" y2="0">
      <stop offset="0" stop-color="#2e1f5e"/>
      <stop offset="0.4" stop-color="#5e1a70"/>
      <stop offset="1" stop-color="#c5359a"/>
    </linearGradient>
  </defs>

  <rect class="label-base" x="125" y="614" width="1248" height="446" fill="var(--white)" stroke="var(--trim)"/>

  <path class="wave-main" d="M125,772 C300,700 520,680 720,745 C920,810 1150,905 1373,895 L1373,1060 L125,1060 Z" fill="url(#wave-gradient)"/>
  <path class="wave-edge" d="M900,800 C1050,860 1220,905 1373,898" fill="none" stroke="var(--plum)" stroke-width="8"/>
  <path class="wave-lower" d="M880,965 C1080,925 1280,940 1373,985 L1373,1060 L880,1060 Z" fill="var(--band-purple)"/>
  <path class="wave-white" d="M530,1060 C720,995 930,945 1130,948 C1250,950 1320,990 1373,1058 L1373,1060 Z" fill="var(--white)"/>

  <g class="nutrition-facts">
    <rect x="177" y="655" width="293" height="367" fill="var(--white)" stroke="var(--ink)" stroke-width="2"/>
    <text class="facts-title" x="197" y="690">Nutrition Facts</text>
    <text class="facts-small" x="197" y="711">Serving Size</text>
    <text class="facts-small" x="457" y="711" text-anchor="end">...g</text>
    <text class="facts-small" x="197" y="727">Servings Per Container</text>
    <rect x="197" y="733" width="261" height="8" fill="var(--ink)"/>
    <text class="facts-bold" x="197" y="758">Amount  Per Serving</text>
    <line x1="197" y1="764" x2="458" y2="764" stroke="var(--ink)"/>
    <text class="facts-bold" x="197" y="780">Calories <tspan class="facts-small">....</tspan></text>
    <text class="facts-small" x="458" y="780" text-anchor="end">Calories from Fat ...</text>
    <rect x="197" y="786" width="261" height="4" fill="var(--ink)"/>
    <text class="facts-tiny" x="457" y="802" text-anchor="end">% Daily Value*</text>
    <line x1="197" y1="808" x2="458" y2="808" stroke="var(--ink)"/>
    <text class="facts-bold" x="197" y="824">Total Fat <tspan class="facts-small">...g</tspan></text>
    <text class="facts-bold" x="457" y="826" text-anchor="end">...%</text>
    <line x1="218" y1="829" x2="458" y2="829" stroke="var(--ink)"/>
    <text class="facts-small" x="219" y="845">Saturated Fat ...g</text>
    <text class="facts-bold" x="457" y="845" text-anchor="end">...%</text>
    <line x1="218" y1="850" x2="458" y2="850" stroke="var(--ink)"/>
    <text class="facts-small" x="219" y="865"><tspan font-style="italic">Trans</tspan> Fat ...g</text>
    <line x1="197" y1="870" x2="458" y2="870" stroke="var(--ink)"/>
    <text class="facts-bold" x="197" y="886">Cholestrol <tspan class="facts-small">...mg</tspan></text>
    <text class="facts-bold" x="457" y="886" text-anchor="end">...%</text>
    <line x1="197" y1="890" x2="458" y2="890" stroke="var(--ink)"/>
    <text class="facts-bold" x="197" y="905">Sodium <tspan class="facts-small">...mg</tspan></text>
    <text class="facts-bold" x="457" y="905" text-anchor="end">...%</text>
    <line x1="197" y1="910" x2="458" y2="910" stroke="var(--ink)"/>
    <text class="facts-bold" x="197" y="925">Total Carbohydrate <tspan class="facts-small">...g</tspan></text>
    <text class="facts-bold" x="457" y="925" text-anchor="end">...%</text>
    <line x1="218" y1="930" x2="458" y2="930" stroke="var(--ink)"/>
    <text class="facts-small" x="219" y="945">Dietary Fiber ...g</text>
    <text class="facts-bold" x="457" y="945" text-anchor="end">...%</text>
    <line x1="218" y1="950" x2="458" y2="950" stroke="var(--ink)"/>
    <text class="facts-small" x="219" y="966">Sugars ...g</text>
    <line x1="197" y1="971" x2="458" y2="971" stroke="var(--ink)"/>
    <text class="facts-bold" x="197" y="987">Protein <tspan class="facts-small">...g</tspan></text>
    <rect x="197" y="994" width="261" height="8" fill="var(--ink)"/>
  </g>

  <text class="product-name" transform="translate(628,995) rotate(-90)" textLength="350" lengthAdjust="spacingAndGlyphs" fill="#ffffff" stroke="#6a1670" stroke-width="3" paint-order="stroke">REVIVE</text>
  <text class="product-sub" transform="translate(698,992) rotate(-90)" textLength="246" lengthAdjust="spacingAndGlyphs" fill="#4b2466" stroke="#ffffff" stroke-width="3" paint-order="stroke">SPARK</text>
  <rect class="variant-tag" x="550" y="1008" width="152" height="28" fill="var(--band-purple)"/>
  <text class="variant" x="626" y="1031" text-anchor="middle">OMEGA - 3</text>
  <text class="net-weight" x="889" y="1038" text-anchor="middle">400g</text>

  <g class="brand">
    <circle cx="851" cy="712" r="77" fill="var(--grape)" stroke="var(--white)" stroke-width="6"/>
    <text class="brand-name" x="851" y="724" text-anchor="middle">Lumo</text>
  </g>

  <g class="badge badge-eye">
    <circle cx="766" cy="792" r="43" fill="var(--cyan)" stroke="var(--white)" stroke-width="5"/>
    <path d="M733,792 Q766,765 799,792 Q766,819 733,792 Z" fill="none" stroke="var(--white)" stroke-width="4"/>
    <circle cx="766" cy="792" r="9" fill="var(--white)"/>
  </g>
  <g class="badge badge-heart">
    <circle cx="882" cy="845" r="38" fill="var(--rose)" stroke="var(--white)" stroke-width="5"/>
    <path d="M882,868 C860,852 858,840 862,832 C867,823 878,823 882,832 C886,823 897,823 902,832 C906,840 904,852 882,868 Z" fill="none" stroke="var(--white)" stroke-width="4" stroke-linejoin="round"/>
  </g>
  <g class="badge badge-brain">
    <circle cx="795" cy="895" r="49" fill="var(--yellow)" stroke="var(--white)" stroke-width="5" role="img" aria-label="Brain illustration for cognitive support"/>
  </g>

  <g class="body-copy">
    <text x="1012" y="682" textLength="325" lengthAdjust="spacing">Lorem ipsum dolor sit amet, consectetur adipiscing</text>
    <text x="1012" y="698" textLength="325" lengthAdjust="spacing">elit, sed do eiusmod tempor incididunt ut labore et</text>
    <text x="1012" y="714" textLength="325" lengthAdjust="spacing">dolore magna aliqua. Ut enim ad minim veniam, quis</text>
    <text x="1012" y="730" textLength="325" lengthAdjust="spacing">nostrud exercitation ullamco laboris nisi ut aliquip ex</text>
    <text x="1012" y="746" textLength="325" lengthAdjust="spacing">ea commodo consequat. Duis aute irure dolor in</text>
    <text x="1012" y="762" textLength="325" lengthAdjust="spacing">reprehenderit in voluptate velit esse cillum dolore eu</text>
    <text x="1012" y="778" textLength="325" lengthAdjust="spacing">fugiat nulla pariatur. Excepteur sint occaecat</text>
    <text x="1012" y="794" textLength="325" lengthAdjust="spacing">cupidatat non proident, sunt in culpa qui officia</text>
    <text x="1012" y="810">deserunt mollit anim id est laborum</text>
    <text x="1012" y="1013">Lorem ipsum dolor sit amet,</text>
    <text x="1012" y="1028">tempor incididunt ut labore</text>
    <text x="1012" y="1043">quis nostrud exercitation</text>
  </g>
</svg>
</body>
</html>
```